Letterhead & Business Card for our Professional Practice (Financial Services)

We are looking for someone to design a letterhead and business card for our business, which is a professional practice called Harbor Lumen Capital Limited. The website is at www.harborrlumencapital.example.co.uk.

The letterhead needs to have: (a) our logo (b) address (c) telephone number (d) email address and (e) our company number.

We would like the stationary to be consistent with the website.

I have attached the logo in EPS and PNG format.

Target Market(s)

Professional services, large commercial enterprises, financial services

Industry/Entity Type

Financial Service

Font styles to use
Serif

Colors
3176b5
f04a50

Requirements
Must have
• Be consistent with our website located at www.harborlumencapital.example.co.uk
• Be in the following formats:
• 1. Word template for the letterhead
• 2. PDF for the letterhead with setup and bleeds required at www.presskite.example.co.uk
• 3. PDF for the business card with setup and bleeds required at www.presskite.example.co.uk
Nice to have
• Something with a really interesting design that says "these guys are professional but dynamic and interesting"
Should not have
• Boring

```html
<!DOCTYPE html>
<html lang="en">
<head>
<meta charset="utf-8">
<title>Harbor Lumen Capital – Business Card</title>
<link rel="stylesheet" href="https://fonts.googleapis.com/css2?family=PT+Sans:ital,wght@0,400;0,700;1,400&display=swap">
<style>
  :root {
    --backdrop: #3b3b3b;
    --card: #ebeae6;
    --navy: #1d4877;
    --red: #d2202f;
    --body-text: #555555;
    --tint-blue: #c9d6e2;
    --tint-red: #e7c6c6;
  }
  * { margin: 0; padding: 0; box-sizing: border-box; }
  html, body {
    width: 1105px;
    height: 1200px;
    overflow: hidden;
    background: var(--backdrop);
    font-family: "PT Sans", sans-serif;
  }
  .card {
    position: absolute;
    left: 192px;
    width: 720px;
    height: 411px;
    background: var(--card);
    overflow: hidden;
  }
  .card--front { top: 150px; }
  .card--back { top: 620px; }
  .card__texture {
    position: absolute;
    inset: 0;
    background: linear-gradient(180deg, #edece8 0%, #e8e7e3 100%);
  }
  .brand {
    position: absolute;
    left: 0; right: 0;
    top: 170px;
    display: flex;
    align-items: center;
    justify-content: center;
    gap: 16px;
  }
  .brand__square {
    width: 34px;
    height: 34px;
    background: var(--red);
  }
  .brand__name {
    font-weight: 700;
    font-size: 40px;
    color: var(--navy);
    letter-spacing: 0.2px;
  }
  .card__shapes {
    position: absolute;
    inset: 0;
  }
  .contact {
    position: absolute;
    left: 0; right: 0;
    top: 0;
    text-align: center;
  }
  .contact__name {
    position: absolute;
    left: 0; right: 0;
    top: 100px;
    font-weight: 700;
    font-size: 27px;
    color: var(--navy);
    letter-spacing: 0.5px;
  }
  .contact__role {
    position: absolute;
    left: 0; right: 0;
    top: 137px;
    font-size: 16px;
    color: var(--red);
  }
  .rule {
    position: absolute;
    left: 133px;
    width: 462px;
    height: 1.5px;
  }
  .rule--navy { top: 170px; background: var(--navy); }
  .rule--red { top: 268px; background: var(--red); }
  .contact__line {
    position: absolute;
    left: 0; right: 0;
    font-size: 16.5px;
    color: var(--body-text);
  }
  .contact__address { top: 184px; }
  .contact__phone { top: 208px; }
  .contact__web { top: 233px; letter-spacing: 2.4px; }
  .contact__tagline {
    position: absolute;
    left: 0; right: 0;
    top: 284px;
    font-style: italic;
    font-size: 16.5px;
    line-height: 23px;
    color: var(--body-text);
  }
</style>
</head>
<body>
  <section class="card card--front">
    <div class="card__texture" role="img" aria-label="Fine light grey hexagon pattern covering the card"></div>
    <div class="brand">
      <span class="brand__square"></span>
      <span class="brand__name">Harbor Lumen Capital</span>
    </div>
  </section>

  <section class="card card--back">
    <div class="card__texture" role="img" aria-label="Fine light grey hexagon pattern covering the card"></div>
    <svg class="card__shapes" width="720" height="411" viewBox="0 0 720 411">
      <rect x="253" y="0" width="467" height="352" fill="var(--tint-blue)" opacity="0.55"/>
      <path d="M0 350 L420 70 Q460 45 468 95 L520 411 L0 411 Z" fill="var(--tint-red)" opacity="0.55"/>
    </svg>
    <div class="contact">
      <h1 class="contact__name">DANIEL MARSH</h1>
      <p class="contact__role">CEO/FOUNDER</p>
      <div class="rule rule--navy"></div>
      <p class="contact__line contact__address">14-16 Quayside Row, Easton, Berkshire, EB2 7QR</p>
      <p class="contact__line contact__phone">Phone : 01632 960418 Email : info@harborlumencapital.example.co.uk</p>
      <p class="contact__line contact__web">www.harborrlumencapital.example.co.uk</p>
      <div class="rule rule--red"></div>
      <p class="contact__tagline">Security Trustee, administration, nominee and<br>escrow services to the investment &amp; corporate / SME markets.</p>
    </div>
  </section>
</body>
</html>
```